Web design for business website

I need a web design for a business website for one of our clients who is specialized in alarm management software. I would like you to design 3 web pages, one for each of the 3 pages. You need to process the corporate identity of our client to the web design. This means the colors of the logo (red and black) should definitely show up on all of the 3 pages. Find the logo file for the logo of our customer. To increase readability I suggest you use a white/light background. All suggestions are welcome.

Target Market(s)

B2B, Alarm management

Industry/Entity Type

Business

Number of Pages Required

3 page

Requirements
Must have
• The web design must have exactly the same structure as the wireframes and needs to contain the colors of the company logo.

```html
<!DOCTYPE html>
<html lang="en">
<head>
<meta charset="utf-8">
<title>Korvane – Real-time reasoning solutions</title>
<link href="https://fonts.googleapis.com/css2?family=Montserrat:wght@800&family=Open+Sans:wght@400;600&family=Roboto+Condensed:wght@400;700&display=swap" rel="stylesheet">
<style>
:root{
  --navy:#1d1c36;
  --navy-panel:#2b2a47;
  --orange:#e8461b;
  --ink:#24233d;
  --text:#666;
  --line:#d9d9d9;
  --nav-bg:#f7f7f7;
  --white:#fff;
  --foot-text:#e6e6ee;
}
*{box-sizing:border-box;margin:0;padding:0}
html,body{width:762px;height:1200px;overflow:hidden;background:var(--white)}
body{position:relative;font-family:"Open Sans",sans-serif;color:var(--text)}
.abs{position:absolute}

/* top bar */
.topbar{left:0;top:0;width:762px;height:36px;background:var(--navy);color:var(--white);font-size:10px}
.topbar .phone{left:36px;top:9px;display:flex;align-items:center;gap:8px}
.topbar .lang{left:465px;top:12px;font-size:9px;font-weight:600;display:flex;align-items:center;gap:6px}
.flag{width:11px;height:8px;background:#c8cbe0;display:inline-block}
.search{left:537px;top:6px;width:188px;height:23px;background:var(--white);display:flex}
.search span{flex:1;font-size:9px;font-style:italic;color:#555;padding:6px 9px}
.search b{width:21px;background:var(--orange);display:flex;align-items:center;justify-content:center}

/* header */
.brand{left:36px;top:63px;display:flex;align-items:center;gap:15px}
.brand-dot{width:47px;height:47px;border-radius:50%;background:var(--orange)}
.brand-name{font-family:"Montserrat",sans-serif;font-weight:800;font-size:33px;letter-spacing:2px;color:var(--ink);line-height:1}
.brand-tag{font-size:10px;color:var(--ink);margin-top:4px;letter-spacing:.3px}
.user-btn{top:67px;width:37px;height:37px;border-radius:50%;background:#c9c9c9;color:var(--white);font-size:7.5px;text-align:center;padding-top:8px}
.user-btn.active{background:var(--orange)}
.user-btn svg{display:block;margin:0 auto 1px}

/* nav */
.nav{left:0;top:137px;width:762px;height:35px;background:var(--nav-bg);border-top:1px solid #e6e6e6;border-bottom:1px solid #e6e6e6}
.nav a{position:absolute;top:0;height:34px;line-height:34px;text-align:center;font-family:"Roboto Condensed",sans-serif;font-size:12px;color:#555;text-decoration:none;border-right:1px solid #e3e3e3}
.nav a.current{background:var(--orange);color:var(--white);height:35px}

/* hero */
.hero{left:0;top:172px;width:762px;height:392px;background:linear-gradient(180deg,#233156 0%,#41506a 30%,#8c8c6a 55%,#6a7a70 75%,#3c4650 100%)}
.hero-arrow{top:354px;width:28px;height:28px;border-radius:50%;background:var(--white);display:flex;align-items:center;justify-content:center}

/* sections */
.section-title{font-family:"Roboto Condensed",sans-serif;font-weight:700;font-size:16px;color:#555}
.section-title em{font-style:normal;color:var(--orange)}
.rule{height:2px;background:var(--line)}
.rule i{display:block;height:2px;background:var(--orange)}
.intro{left:37px;top:630px;width:690px;font-size:9px;line-height:16.5px;color:#6b6b6b}

.clients{left:36px;top:797px;width:688px;height:83px;background:var(--white);box-shadow:0 0 5px rgba(0,0,0,.25);display:flex;align-items:center;justify-content:space-between;padding:0 42px}
.client{display:flex;align-items:center;gap:6px;font-size:15px;font-weight:600;color:var(--ink);white-space:nowrap}
.client i{width:9px;height:9px;background:var(--orange);display:inline-block}
.client-arrow{top:823px;width:30px;height:32px;background:var(--white);border-radius:50%;box-shadow:0 0 4px rgba(0,0,0,.3);display:flex;align-items:center;justify-content:center}

/* footer */
.footer{left:0;top:915px;width:762px;height:285px;background:var(--navy)}
.social{top:937px;width:23px;height:23px;border-radius:50%;border:1px solid #8a89a3}
.social.first{background:var(--orange);border-color:var(--orange)}
.newsletter-label{left:435px;top:943px;font-family:"Roboto Condensed",sans-serif;font-size:12.5px;color:var(--orange)}
.newsletter{left:513px;top:937px;width:212px;height:27px;display:flex;background:#1a1930;border:1px solid #3a3958}
.newsletter span{flex:1;color:var(--white);font-size:10px;padding:6px 8px}
.newsletter b{width:33px;background:var(--orange);display:flex;align-items:center;justify-content:center}
.panel{left:37px;top:985px;width:688px;height:170px;background:var(--navy-panel)}
.col{position:absolute;top:1002px}
.col h4{font-family:"Roboto Condensed",sans-serif;font-size:12.5px;font-weight:400;color:var(--orange);padding-bottom:5px;border-bottom:1px solid #45446a;margin-bottom:7px;white-space:nowrap}
.col ul{list-style:none}
.col li{font-size:9px;color:var(--foot-text);height:22.6px;line-height:22.6px;display:flex;align-items:center;gap:8px;white-space:nowrap}
.col li::before{content:"";width:4px;height:4px;border:1px solid #bbb;display:inline-block}
.contact{position:absolute;left:553px;width:165px;display:flex;gap:10px;font-size:9px;color:var(--foot-text);line-height:14px}
.contact svg{flex:none}
.copyright{left:37px;top:1171px;font-size:9px;color:#8d8ca6}
.card{top:1168px;width:26px;height:18px;border-radius:2px;background:#d7dae6}
</style>
</head>
<body>

<div class="abs topbar">
  <div class="abs phone">
    <svg width="17" height="17" viewBox="0 0 17 17"><circle cx="8.5" cy="8.5" r="7.5" fill="none" stroke="#fff"/><path d="M6 5l1.3 1.8-.8 1c.5 1 1.3 1.8 2.3 2.3l1-.8L11.6 10.6 10.9 12C8 11.5 5.5 9 5 6.2z" fill="#fff"/></svg>
    +31 (0)85 4410 372
  </div>
  <div class="abs lang"><span class="flag"></span>ENGLISH <svg width="6" height="4"><path d="M0 0h6L3 4z" fill="#fff"/></svg></div>
  <div class="abs search"><span>Search....</span><b><svg width="12" height="12" viewBox="0 0 12 12"><circle cx="7" cy="5" r="3.6" fill="none" stroke="#fff" stroke-width="1.4"/><path d="M4.4 7.6L1.5 10.5" stroke="#fff" stroke-width="1.5"/></svg></b></div>
</div>

<header>
  <div class="abs brand">
    <span class="brand-dot"></span>
    <div>
      <div class="brand-name">KORVANE</div>
      <div class="brand-tag">Real-time reasoning solutions</div>
    </div>
  </div>
  <div class="abs user-btn active" style="left:602px"><svg width="10" height="10" viewBox="0 0 10 10"><circle cx="5" cy="3" r="2.5" fill="#fff"/><path d="M0 10c0-3 2-4.5 5-4.5s5 1.5 5 4.5z" fill="#fff"/></svg>Account</div>
  <div class="abs user-btn" style="left:646px"><svg width="10" height="10" viewBox="0 0 10 10"><rect x="1.5" y="4.5" width="7" height="5.5" fill="#fff"/><path d="M3 4.5V3a2 2 0 014 0v1.5" fill="none" stroke="#fff" stroke-width="1.3"/></svg>Login</div>
  <div class="abs user-btn" style="left:689px"><svg width="11" height="10" viewBox="0 0 11 10"><circle cx="4.5" cy="3" r="2.5" fill="#fff"/><path d="M0 10c0-3 2-4.5 4.5-4.5S9 7 9 10z" fill="#fff"/><path d="M9.5 1v3M8 2.5h3" stroke="#fff"/></svg>Sing up</div>
</header>

<nav class="abs nav">
  <a class="current" style="left:37px;width:89px">HOME</a>
  <a style="left:126px;width:109px">INDUSTRY</a>
  <a style="left:235px;width:114px">TELECOM</a>
  <a style="left:349px;width:94px">POWER</a>
  <a style="left:443px;width:103px">UTILTIES</a>
  <a style="left:546px;width:88px">INFRA</a>
  <a style="left:634px;width:91px">STORE</a>
</nav>

<div class="abs hero" role="img" aria-label="Photo of an illuminated oil refinery with towers and pipework at night"></div>
<div class="abs hero-arrow" style="left:36px"><svg width="8" height="12"><path d="M6.5 1L1.5 6l5 5" fill="none" stroke="#e8461b" stroke-width="1.4"/></svg></div>
<div class="abs hero-arrow" style="left:698px"><svg width="8" height="12"><path d="M1.5 1l5 5-5 5" fill="none" stroke="#e8461b" stroke-width="1.4"/></svg></div>

<h2 class="abs section-title" style="left:37px;top:588px">WELCOME TO <em>KORVANE</em></h2>
<div class="abs rule" style="left:37px;top:616px;width:688px"><i style="width:124px"></i></div>
<p class="abs intro">Companies have invested to get data out of processes. New technologies have been developed to get real-time data out of the harshest places, like oil-well drill heads or the Great Barrier Riff. Data in itself means nothing without the context the data is collected in. Example: data from equipment under maintnance does not provide information to operations. Information - data which is valid and meaningful - can overwhelm any user without the proper knowledge to interpret this information. Korvane technology enables easy application of such knowledge in a comprehensible – visual – representation and makes hypothetical reasoning with information possible providing meaningful advisories to subscribers when they need it or when it is required that they are made aware of a situation which requires their attention.</p>

<h2 class="abs section-title" style="left:37px;top:746px">OUR <em>CLIENTS</em></h2>
<div class="abs rule" style="left:37px;top:774px;width:688px"><i style="width:118px"></i></div>

<div class="abs clients">
  <div class="client">Brouwvelt</div>
  <div class="client"><i></i>Solvane</div>
  <div class="client"><i></i>Maravik Oil</div>
  <div class="client"><i></i>Dexamo</div>
  <div class="client">Lindqvell</div>
  <div class="client">Conchar</div>
</div>
<div class="abs client-arrow" style="left:24px"><svg width="8" height="12"><path d="M6.5 1L1.5 6l5 5" fill="none" stroke="#222" stroke-width="2"/></svg></div>
<div class="abs client-arrow" style="left:708px"><svg width="8" height="12"><path d="M1.5 1l5 5-5 5" fill="none" stroke="#222" stroke-width="2"/></svg></div>

<footer>
  <div class="abs footer"></div>
  <span class="abs social first" style="left:37px"></span>
  <span class="abs social" style="left:66px"></span>
  <span class="abs social" style="left:95px"></span>
  <span class="abs social" style="left:124px"></span>
  <span class="abs social" style="left:152px"></span>
  <span class="abs social" style="left:181px"></span>
  <div class="abs newsletter-label">NEWSLETTER</div>
  <div class="abs newsletter"><span>@email_address</span><b><svg width="16" height="14" viewBox="0 0 16 14"><path d="M0 6L16 0 12 14 8 9z" fill="#fff"/></svg></b></div>

  <div class="abs panel"></div>
  <div class="col" style="left:50px;width:128px"><h4>SOLUTIONS</h4><ul><li>ARQ Alarm Reporting</li><li>ARQ Alarm Analysis</li><li>ARQ Alarm Expert</li><li>Use</li></ul></div>
  <div class="col" style="left:198px;width:72px"><h4>INDUSTRIES</h4><ul><li>Industry</li><li>Telceom</li><li>Power</li><li>Infra</li></ul></div>
  <div class="col" style="left:321px;width:62px"><h4>ABOUT US</h4><ul><li>Compnay</li><li>Overview</li><li>Leadership</li><li>Partners</li><li>Locations</li></ul></div>
  <div class="col" style="left:436px;width:80px"><h4>NEWS</h4><ul><li>Product News</li><li>Partner News</li><li>Events</li><li>Press Releases</li><li>Vacancies</li></ul></div>
  <div class="col" style="left:547px;width:160px"><h4>CONTACTS INFORMATIONS</h4></div>
  <div class="contact" style="top:1035px"><svg width="20" height="20" viewBox="0 0 20 20"><path d="M9 2h2v16H9zM3 5h13l2 2-2 2H3zM5 10h11v3H5z" fill="#e8461b"/></svg><span>Korvane Suite 4, Lorem econse<br>Post Box 581 NEWTON 4821</span></div>
  <div class="contact" style="top:1081px;align-items:center"><svg width="20" height="18" viewBox="0 0 20 18"><path d="M3 2l3 4-1.5 1.5c1 2.2 2.8 4 5 5L11 11l4 3-1.5 3C8 16 3.5 11 2.5 4z" fill="#e8461b"/><path d="M12 2a5 5 0 014 4M12 5a2 2 0 011.5 1.5" stroke="#e8461b" fill="none"/></svg>+31 (0)85 4410 372</div>
  <div class="contact" style="top:1118px;align-items:center"><svg width="20" height="14" viewBox="0 0 20 14"><rect x=".5" y=".5" width="19" height="13" fill="none" stroke="#e8461b"/><path d="M.5 .5l9.5 8 9.5-8M.5 13.5l7-6M19.5 13.5l-7-6" stroke="#e8461b" fill="none"/></svg>info@korvane.com</div>

  <div class="abs copyright">Copyright © 2015 korvane.com | All Rights Reserved.</div>
  <span class="abs card" style="left:549px"></span>
  <span class="abs card" style="left:579px"></span>
  <span class="abs card" style="left:609px"></span>
  <span class="abs card" style="left:639px"></span>
  <span class="abs card" style="left:669px"></span>
  <span class="abs card" style="left:699px"></span>
</footer>

</body>
</html>
```